Location services company card

Design a new business card for our location services company. I would like to have the front fairly standard with phone and email, logo, name, title etc. Back should feature text: "Location intelligence: make better decisions with maps." I would like either a location pin on the back to make it obvious that we are involved with maps. This could also have a small mud map on the back (use Vensu.com for design inspiration here).

Target Market(s)

Business and government

Industry/Entity Type

Consultant

Contact Information for Business Card

Name, title, address, phone, mobile, email

Font styles to use
Sans Serif

Requirements
Must have
• Flat design with the company colours:
• C60 M0 Y100 K0 and C100 M20 Y0 K65
• Location pin and/or mud map on back.
• Design must be similar/consistent in feel to tqav.com.au

```html
<!DOCTYPE html>
<html lang="en">
<head>
<meta charset="utf-8">
<title>TQAV Business Card</title>
<link href="https://fonts.googleapis.com/css2?family=Montserrat:wght@400;500;700&display=swap" rel="stylesheet">
<style>
  :root {
    --brand-green: #66b33a;
    --brand-navy: #003f5c;
    --paper: #f4f4f2;
    --backdrop: #d9d9d9;
    --pin-shadow: #9a9a9a;
    --white: #ffffff;
  }
  * { margin: 0; padding: 0; box-sizing: border-box; }
  html, body {
    width: 1200px; height: 900px; overflow: hidden;
    background: var(--backdrop);
    font-family: "Montserrat", sans-serif;
  }
  .stage {
    position: relative; width: 1200px; height: 900px;
    display: flex; justify-content: center; align-items: center; gap: 90px;
  }
  .card {
    position: relative; width: 320px; height: 560px;
    background: var(--paper); overflow: hidden;
    box-shadow: 0 6px 18px rgba(0,0,0,0.12);
  }

  /* Back */
  .card-back .message {
    position: absolute; left: 50%; top: 50%;
    width: 460px;
    transform: translate(-50%, -50%) rotate(90deg);
    display: flex; align-items: center; justify-content: center; gap: 22px;
  }
  .pin-mark { width: 70px; height: 80px; flex: none; transform: rotate(-90deg); }
  .tagline { color: var(--brand-navy); font-size: 18px; line-height: 1.3; }
  .tagline strong { font-weight: 700; display: block; }
  .tagline span { font-weight: 400; display: block; }

  /* Front */
  .brand {
    position: absolute; top: 0; left: 0; width: 100%; height: 258px;
    display: flex; align-items: center; justify-content: center;
  }
  .brand-name {
    display: inline-flex; align-items: center; gap: 10px;
    font-size: 58px; font-weight: 700; color: var(--brand-navy);
    letter-spacing: -1px; line-height: 1;
  }
  .brand-dot { width: 18px; height: 18px; border-radius: 50%; background: var(--brand-green); }
  .name-band {
    position: absolute; top: 258px; left: 0; width: 100%; height: 68px;
    background: var(--brand-navy);
    display: flex; align-items: center; justify-content: center;
    color: var(--white); font-size: 22px; font-weight: 700;
  }
  .contact-panel {
    position: absolute; top: 326px; left: 0; width: 100%; height: 184px;
    background: var(--brand-green);
    padding: 28px 34px 0;
    color: var(--white); font-size: 14px; font-weight: 500; line-height: 1.4;
    list-style: none;
  }
  .contact-panel li { display: flex; align-items: flex-start; gap: 12px; margin-bottom: 16px; }
  .contact-panel svg { width: 14px; height: 14px; flex: none; margin-top: 3px; }
</style>
</head>
<body>
<main class="stage">

  <section class="card card-back" aria-label="Card back">
    <div class="message">
      <svg class="pin-mark" viewBox="0 0 70 80" aria-hidden="true">
        <ellipse cx="30" cy="68" rx="22" ry="6" fill="var(--pin-shadow)" opacity="0.6"/>
        <path d="M35 4 a22 22 0 0 1 22 22 c0 16 -22 42 -22 42 s-22 -26 -22 -42 a22 22 0 0 1 22 -22z" fill="var(--brand-green)"/>
        <circle cx="35" cy="25" r="7" fill="var(--paper)"/>
      </svg>
      <p class="tagline">
        <strong>Location intelligence:</strong>
        <span>make better decisions with maps.</span>
      </p>
    </div>
  </section>

  <section class="card card-front" aria-label="Card front">
    <div class="brand">
      <div class="brand-name"><span>tqav</span><i class="brand-dot"></i></div>
    </div>
    <div class="name-band">John Doe</div>
    <ul class="contact-panel">
      <li>
        <svg viewBox="0 0 24 24" aria-hidden="true"><path fill="var(--brand-navy)" d="M6.6 10.8a15 15 0 0 0 6.6 6.6l2.2-2.2c.3-.3.7-.4 1-.2 1.1.4 2.3.6 3.6.6.6 0 1 .4 1 1V20c0 .6-.4 1-1 1A17 17 0 0 1 3 4c0-.6.4-1 1-1h3.5c.6 0 1 .4 1 1 0 1.3.2 2.5.6 3.6.1.3 0 .7-.2 1z"/></svg>
        <span>+61 8 9000 4210</span>
      </li>
      <li>
        <svg viewBox="0 0 24 24" aria-hidden="true"><path fill="var(--brand-navy)" d="M12 2a7 7 0 0 1 7 7c0 5-7 13-7 13S5 14 5 9a7 7 0 0 1 7-7zm0 4.5a2.5 2.5 0 1 0 0 5 2.5 2.5 0 0 0 0-5z"/></svg>
        <span>2b/18 Harlow Road<br>Ellerby WA 6100, Australia</span>
      </li>
      <li>
        <svg viewBox="0 0 24 24" aria-hidden="true"><path fill="var(--brand-navy)" d="M2 5h20v14H2z"/><path fill="none" stroke="var(--brand-green)" stroke-width="1.6" d="M2 5l10 8 10-8"/></svg>
        <span>info@tqav.com.au</span>
      </li>
    </ul>
  </section>

</main>
</body>
</html>
```